Glanmor Ridge Outdoor Activity Centre requires a website

Design website including integration with CRM (Leadnest), payments (PayBrio), bookings, social media etc. I already own the main domain together with several subsidiaries that will need linking. Our company is a social enterprise providing adventure sports activities to the local community and beyond. We have a strong focus on opportunities for young people, especially targeting lower socioeconomic demographics by providing affordable access to our activities.
The Glanmor Ridge Outdoor Activity Centre is based in Port Talbot, Wales and aims to provide affordable access to adventure activities using the surrounding area. We work closely with our local community to support education, training and personal growth opportunities for all through adventurous activities.
Target Market(s)
Adventure sports community, young people, education
Requirements
Must have
- Appeal to young people
social media integration
minimalist design
CRM integration
payments/booking integration

```html
<!DOCTYPE html>
<html lang="en">
<head>
<meta charset="utf-8">
<title>Glanmor Ridge Outdoor Activity Centre</title>
<link rel="stylesheet" href="https://fonts.googleapis.com/css2?family=Archivo+Black&family=IBM+Plex+Sans:wght@400;500;600;700&display=swap">
<style>
:root{
  --orange:#f26b1d;
  --blue:#1ea4e0;
  --pink:#e6197a;
  --navy:#1d2a55;
  --ink:#1f1f1f;
  --muted:#555;
  --footer:#1c1c1c;
  --white:#fff;
}
*{box-sizing:border-box;margin:0;padding:0}
html,body{width:1200px;height:4484px;overflow:hidden;background:var(--white)}
body{font-family:"IBM Plex Sans",sans-serif;color:var(--ink)}
.page{position:relative;width:1200px;height:4484px;overflow:hidden}
.abs{position:absolute}
.btn{position:absolute;background:var(--orange);color:var(--white);font-weight:600;font-size:14px;display:flex;align-items:center;justify-content:center;letter-spacing:.3px}
.btn-outline{position:absolute;border:2px solid var(--orange);color:var(--orange);font-weight:700;font-size:11px;display:flex;align-items:center;justify-content:center;letter-spacing:.4px}
.section-title{position:absolute;left:0;width:1200px;text-align:center;font-weight:700;font-size:21px;letter-spacing:.3px}
.section-title::after{content:"";display:block;width:44px;height:3px;background:var(--blue);margin:12px auto 0}

/* header */
.topbar{left:0;top:0;width:1200px;height:4px;background:linear-gradient(90deg,var(--orange) 0 33%,var(--pink) 33% 66%,var(--blue) 66%)}
.brand{left:130px;top:30px;display:flex;align-items:center;gap:10px}
.brand-mark{width:14px;height:14px;background:var(--orange)}
.brand-name{color:var(--orange);font-weight:600;font-size:13px;line-height:15px;width:150px}
.follow{left:503px;top:30px;display:flex;align-items:center;gap:7px;font-size:11px}
.social-dot{width:24px;height:24px;border-radius:50%;background:var(--navy)}
.social-dot.b{background:var(--blue)}
.callus{left:695px;top:18px;display:flex;align-items:center;gap:10px}
.callus small{display:block;font-size:11px;font-weight:600}
.callus strong{display:block;color:var(--orange);font-size:19px;font-weight:600;line-height:20px}
.pill{position:absolute;top:18px;height:34px;border-radius:17px;color:var(--white);font-size:13px;display:flex;align-items:center;justify-content:center}
.nav{left:476px;top:70px;display:flex;gap:40px;font-size:13.5px;font-weight:600}
.nav .active{color:var(--orange);border-bottom:2px solid var(--orange);padding-bottom:2px}

/* hero */
.hero{left:0;top:102px;width:1200px;height:601px;background:linear-gradient(135deg,#5d6b58 0%,#3e5a62 35%,#6f8d8f 60%,#8a948a 100%)}
.hero-title{left:714px;top:258px;font-family:"Archivo Black",sans-serif;color:var(--white);font-size:53px;line-height:60px}
.dots{display:flex;gap:10px;align-items:center}
.dots i{width:6px;height:6px;border-radius:50%;background:var(--white)}
.dots i.on{width:11px;height:11px;background:var(--orange);border:2px solid var(--white)}

/* activities */
.tile{position:absolute;width:238px;height:250px}
.tile span{position:absolute;left:17px;bottom:16px;color:var(--white);font-size:13px;font-weight:700}
.tile span::before{content:"";position:absolute;left:0;top:-10px;width:44px;height:2px;background:var(--white)}

/* welcome */
.welcome{left:0;top:1432px;width:1200px;height:471px;background:linear-gradient(90deg,#6d7a3f 0%,#5a6f47 30%,#4f8a9a 48%,var(--blue) 60%)}
.welcome-text{left:655px;top:1480px;width:400px;color:var(--white)}
.welcome-text h4{font-size:16px;font-weight:600}
.welcome-text h2{font-size:29px;font-weight:500;margin-top:4px;letter-spacing:.5px}
.welcome-text h2::after{content:"";display:block;width:44px;height:3px;background:var(--white);margin-top:10px}
.welcome-text p{font-size:15.5px;line-height:24px;margin-top:30px}

/* testimonials */
.testimonials{left:0;top:2597px;width:1200px;height:517px;background:linear-gradient(120deg,#3c4a2a 0%,#52633a 40%,#6c7e4a 70%,#4a5a36 100%)}
.quote-box{left:133px;top:2712px;width:470px;height:310px;background:rgba(20,20,20,.82);color:var(--white);padding:32px 36px}
.quote-box .q{font-family:"Archivo Black",sans-serif;font-size:40px;line-height:30px}
.quote-box p{font-size:16px;line-height:23px;margin-top:10px}
.author{display:flex;align-items:center;gap:14px;margin-top:26px}
.author i{width:48px;height:48px;border-radius:50%;background:var(--blue)}
.author b{display:block;font-size:12px}
.author small{font-size:11px;color:#ccc}

/* blog */
.card{position:absolute;top:3228px;width:295px;height:374px;border:1px solid #d8d8d8;background:var(--white)}
.card .img{height:188px}
.card h5{font-size:13px;font-weight:600;margin:25px 25px 0;line-height:17px}
.card p{font-size:12px;color:var(--muted);margin:12px 25px 0;line-height:17px}
.card .btn{left:28px;top:325px;width:86px;height:27px;font-size:10px}

/* cta */
.cta{left:0;top:3645px;width:1200px;height:492px;background:linear-gradient(100deg,#3b3b3b 0%,#5a5a5a 30%,#3e5a7a 55%,#2d4566 100%)}
.cta-title{left:618px;top:3758px;color:var(--white);font-size:29px;font-weight:700;line-height:40px}
.cta-text{left:618px;top:3855px;color:#e8e8e8;font-size:18px;line-height:26px;width:440px}

/* footer */
.footer{left:0;top:4137px;width:1200px;height:347px;background:var(--footer);color:var(--white)}
.f-brand{left:133px;top:4245px;display:flex;align-items:center;gap:14px}
.f-brand .brand-mark{width:24px;height:24px}
.f-brand .brand-name{font-size:22px;line-height:26px;width:240px;font-weight:500}
.f-col h6{font-size:12px;font-weight:700;letter-spacing:.3px;margin-bottom:24px}
.f-col li{list-style:none;font-size:11px;line-height:20px}
.f-item{display:flex;align-items:flex-start;gap:12px;font-size:11px;line-height:14px;margin-bottom:22px}
.f-item i{width:22px;height:22px;border-radius:50%;background:var(--white);flex:none;display:flex;align-items:center;justify-content:center}
.f-rule{left:133px;top:4425px;width:935px;height:1px;background:#3a3a3a}
.copyright{left:0;top:4443px;width:1200px;text-align:center;font-size:10px;color:#bbb}
</style>
</head>
<body>
<main class="page">

  <!-- header -->
  <div class="abs topbar"></div>
  <div class="abs brand"><span class="brand-mark"></span><span class="brand-name">Glanmor Ridge Outdoor Activity Centre</span></div>
  <div class="abs follow"><span>FOLLOW US</span><i class="social-dot"></i><i class="social-dot b"></i><i class="social-dot"></i></div>
  <div class="abs callus">
    <svg width="26" height="26" viewBox="0 0 26 26"><circle cx="13" cy="13" r="12" fill="none" stroke="#f26b1d" stroke-width="1.5"/><path d="M9 8c0 5 4 9 9 9l1-2-3-1-1 1c-2-1-3-2-4-4l1-1-1-3z" fill="#f26b1d"/></svg>
    <div><small>CALL US</small><strong>555.014.2290</strong></div>
  </div>
  <div class="pill" style="left:883px;width:88px;background:var(--blue)">Log in</div>
  <div class="pill" style="left:979px;width:90px;background:var(--orange)">Register</div>
  <nav class="abs nav"><span class="active">HOME</span><span>ABOUT US</span><span>SERVICES</span><span>ACTIVITIES</span><span>BLOG</span><span>CONTACT US</span></nav>

  <!-- hero -->
  <div class="abs hero" role="img" aria-label="Photo of a climber leaping from a cliff above a mountain fjord"></div>
  <h1 class="abs hero-title">ADVENTURE<br>SPORTS<br>ACTIVITIES</h1>
  <div class="btn" style="left:718px;top:463px;width:115px;height:40px">READ MORE</div>
  <div class="abs dots" style="left:562px;top:656px"><i></i><i></i><i class="on"></i><i></i><i></i></div>

  <!-- activities -->
  <h2 class="section-title" style="top:738px">OUR ACTIVITIES</h2>
  <div class="tile" style="left:103px;top:808px;background:linear-gradient(180deg,#8a6b55,#3fa8c8)" role="img" aria-label="Photo of a rock climber on an overhang"><span>LOREM IPSUM</span></div>
  <div class="tile" style="left:352px;top:808px;background:linear-gradient(180deg,#2a3a5a,#1ea4e0)" role="img" aria-label="Photo of a girl on a zip line"><span>LOREM IPSUM</span></div>
  <div class="tile" style="left:602px;top:808px;background:linear-gradient(180deg,#8aa070,#2aa0c8)" role="img" aria-label="Photo of people kayaking"><span>LOREM IPSUM</span></div>
  <div class="tile" style="left:850px;top:808px;background:linear-gradient(180deg,#3a6a5a,#1e8fc8)" role="img" aria-label="Photo of a mountain biker"><span>LOREM IPSUM</span></div>
  <div class="tile" style="left:103px;top:1072px;background:linear-gradient(180deg,#6a6070,#d0a070 50%,#30b0d0)" role="img" aria-label="Photo of a paraglider at sunset"><span>LOREM IPSUM</span></div>
  <div class="tile" style="left:352px;top:1072px;background:linear-gradient(180deg,#6a8a40,#2aa8d8)" role="img" aria-label="Photo of a child on a rope course"><span>LOREM IPSUM</span></div>
  <div class="tile" style="left:602px;top:1072px;background:linear-gradient(180deg,#5a6a30,#2a9ac8)" role="img" aria-label="Photo of hikers in a forest"><span>LOREM IPSUM</span></div>
  <div class="tile" style="left:850px;top:1072px;background:linear-gradient(180deg,#4a5a40,#1e98d0)" role="img" aria-label="Photo of a quad bike rider in woods"><span>LOREM IPSUM</span></div>
  <div class="btn-outline" style="left:526px;top:1355px;width:151px;height:32px">VIEW ALL ACTIVITIES</div>

  <!-- welcome -->
  <div class="abs welcome" role="img" aria-label="Photo of a child crossing a rope bridge, blending into blue"></div>
  <div class="abs welcome-text">
    <h4>WELCOME TO</h4>
    <h2>GLANMOR RIDGE</h2>
    <p>Lorem ipsum dolor sit amet, consectetur adipiscing elit, sed do eiusmod tempor incididunt ut labore et dolore magna aliqua. Ut enim ad minim veniam, quis nostrud exercitation ullamco laboris nisi ut aliquip ex ea commodo consequat. Duis aute irure dolor in reprehenderit in voluptate velit esse cillum dolore eu fugiat nulla pariatur. Excepteur sint occaecat cupidatat non proident, sunt in.</p>
  </div>
  <div class="btn" style="left:659px;top:1810px;width:117px;height:39px">READ MORE</div>

  <!-- gallery -->
  <h2 class="section-title" style="top:1945px">GALLERY</h2>
  <div class="abs" style="left:139px;top:2014px;width:448px;height:448px;background:linear-gradient(160deg,#c8d0d8,#9a8a70 60%,#7a5a3a)" role="img" aria-label="Photo of a motocross rider jumping"></div>
  <div class="abs" style="left:603px;top:2014px;width:216px;height:216px;background:linear-gradient(180deg,#b8d4e8,#2a6aa0)" role="img" aria-label="Photo of a windsurfer"></div>
  <div class="abs" style="left:835px;top:2014px;width:216px;height:216px;background:linear-gradient(160deg,#d8d0c0,#8a8a60)" role="img" aria-label="Photo of a paintball player aiming"></div>
  <div class="abs" style="left:603px;top:2246px;width:216px;height:216px;background:linear-gradient(180deg,#9ab8c8,#2a5a80)" role="img" aria-label="Photo of a jet ski rider"></div>
  <div class="abs" style="left:835px;top:2246px;width:216px;height:216px;background:linear-gradient(160deg,#4a6a4a,#8a8a80)" role="img" aria-label="Photo of a mountain bike wheel on a trail"></div>
  <div class="btn" style="left:542px;top:2497px;width:116px;height:40px">VIEW ALL</div>

  <!-- testimonials -->
  <div class="abs testimonials" role="img" aria-label="Photo of two people riding a zip line over a forest"></div>
  <h2 class="abs" style="left:133px;top:2640px;color:#fff;font-size:21px;font-weight:600">TESTIMONIALS</h2>
  <div class="abs" style="left:133px;top:2673px;width:470px;height:1px;background:rgba(255,255,255,.5)"></div>
  <div class="abs quote-box">
    <div class="q">“</div>
    <p>Lorem ipsum dolor sit amet, consectetur adipis cing elit, sed do eiusmod tempor incididunt ut labore et dolore magna aliqua. Ut enim ad minim veniam, quis nostrud exercitation ullamco laboris nisi ut aliquip ex ea commodo consequat. Duis aute irure dolor in reprehenderit in voluptate velit esse.</p>
    <div class="author"><i></i><div><b>RHYS</b><small>Wales</small></div></div>
  </div>
  <div class="abs dots" style="left:324px;top:3055px"><i></i><i></i><i style="background:var(--orange)"></i><i></i><i></i></div>

  <!-- blog -->
  <h2 class="section-title" style="top:3150px">LATEST BLOG</h2>
  <article class="card" style="left:133px"><div class="img" style="background:linear-gradient(180deg,#8aa0a8,#1a4a5a)" role="img" aria-label="Photo of a kayaker on a lake"></div><h5>LOREM IPSUM DOLOR SIT AMET CONSECTETUR ADIPISCING</h5><p>Excepteur sint occaecat cupidatat non proident, sunt in culpa qui officia dese runt mollit anim id est laborum</p><div class="btn">READ MORE</div></article>
  <article class="card" style="left:453px"><div class="img" style="background:linear-gradient(180deg,#5a6a5a,#d8dce0)" role="img" aria-label="Photo of cyclists riding through snow"></div><h5>LOREM IPSUM DOLOR SIT AMET CONSECTETUR ADIPISCING</h5><p>Excepteur sint occaecat cupidatat non proident, sunt in culpa qui officia dese runt mollit anim id est laborum</p><div class="btn">READ MORE</div></article>
  <article class="card" style="left:774px"><div class="img" style="background:linear-gradient(180deg,#6a9a40,#3a5a2a)" role="img" aria-label="Photo of a child on a tree-top course"></div><h5>LOREM IPSUM DOLOR SIT AMET CONSECTETUR ADIPISCING</h5><p>Excepteur sint occaecat cupidatat non proident, sunt in culpa qui officia dese runt mollit anim id est laborum</p><div class="btn">READ MORE</div></article>

  <!-- call to action -->
  <div class="abs cta" role="img" aria-label="Photo of a climber on a rock face against a cloudy sky"></div>
  <h2 class="abs cta-title">LOREM IPSUM DOLOR SIT AMET<br>CONSECTETUR ADIPISCING</h2>
  <p class="abs cta-text">Excepteur sint occaecat cupidatat non proident, sunt in culpa qui officia dese runt mollit.</p>
  <div class="btn" style="left:625px;top:3932px;width:119px;height:39px">CONTACT US</div>

  <!-- footer -->
  <footer class="abs footer"></footer>
  <div class="abs f-brand"><span class="brand-mark"></span><span class="brand-name">Glanmor Ridge Outdoor Activity Centre</span></div>
  <div class="abs f-col" style="left:465px;top:4186px;color:#fff">
    <h6>MENU</h6>
    <ul><li>HOME</li><li>ABOUT US</li><li>SERVICES</li><li>ACTIVITIES</li><li>BLOG</li><li>CONTACT US</li></ul>
  </div>
  <div class="abs f-col" style="left:685px;top:4186px;color:#fff">
    <h6>CONTACT US</h6>
    <div class="f-item"><i><svg width="10" height="12" viewBox="0 0 10 12"><path d="M5 0a4 4 0 0 0-4 4c0 3 4 8 4 8s4-5 4-8a4 4 0 0 0-4-4zm0 5.5A1.5 1.5 0 1 1 5 2.5a1.5 1.5 0 0 1 0 3z" fill="#1c1c1c"/></svg></i><span>27 Harbour Lane<br>Baglan, SA12 7QT</span></div>
    <div class="f-item"><i><svg width="11" height="11" viewBox="0 0 11 11"><path d="M1 1c0 5 4 9 9 9l1-2-3-1-1 1C5 7 4 6 3 4l1-1-1-3z" fill="#1c1c1c"/></svg></i><span>Call Us<br>555.014.2290</span></div>
    <div class="f-item"><i><svg width="11" height="8" viewBox="0 0 11 8"><rect width="11" height="8" fill="#1c1c1c"/><path d="M0 0l5.5 4L11 0" stroke="#fff" fill="none"/></svg></i><span>E mail Us<br>hello@glanmorridge.org</span></div>
  </div>
  <div class="abs f-col" style="left:965px;top:4186px;color:#fff">
    <h6>FOLLOW US</h6>
    <div class="f-item"><i></i><span>Like us on<br>FRIENDBOOK</span></div>
    <div class="f-item"><i></i><span>Follow us on<br>CHIRPER</span></div>
    <div class="f-item"><i></i><span>Follow us on<br>WORKLINK</span></div>
  </div>
  <div class="abs f-rule"></div>
  <div class="abs copyright">Copyright © 2021 All Rights Reserved</div>

</main>
</body>
</html>
```